Harbor Business Cards

I need a business card designed with the following information.

Company Name: Harbor Wealth Management
Name: BriAnne Dockery
Title: Executive Assistant
Cell: (281) 555-0173
Direct Line: (832) 555-0148
Email: brianne@harborwmx.com
Address: 20537 W. Marlowe PKWY Ste. B
Brookvale, HV 77390

I have attached the logo.
I would like it in navy blue and silver.
Thanks.

```html
<!DOCTYPE html>
<html lang="en">
<head>
<meta charset="utf-8">
<title>Harbor Wealth Management – Business Card</title>
<link href="https://fonts.googleapis.com/css2?family=Open+Sans:wght@400;700&display=swap" rel="stylesheet">
<style>
  :root {
    --navy: #13284a;
    --grey-text: #8a8a8a;
    --ink: #3a3a3a;
    --stage: #2b2b2c;
    --paper: #ffffff;
    --silver-light: #e6e6e6;
    --silver-dark: #a9a9a9;
  }
  * { margin: 0; padding: 0; box-sizing: border-box; }
  html, body { width: 1200px; height: 885px; overflow: hidden; }
  body {
    background: var(--stage);
    font-family: "Open Sans", Arial, sans-serif;
    position: relative;
  }
  .card {
    position: absolute;
    box-shadow: 0 10px 30px rgba(0,0,0,.45);
  }

  /* Back side */
  .card-back {
    left: 90px; top: 70px;
    width: 520px; height: 297px;
    background: linear-gradient(160deg, var(--silver-light) 0%, #cfcfcf 45%, var(--silver-dark) 100%);
    display: flex; flex-direction: column; align-items: center; justify-content: center;
  }
  .back-mark {
    width: 46px; height: 46px;
    background: var(--navy);
    margin-bottom: 18px;
  }
  .wordmark {
    color: var(--navy);
    font-weight: 400;
    text-transform: uppercase;
    letter-spacing: .22em;
    text-align: center;
    line-height: 1.3;
    white-space: nowrap;
  }
  .card-back .wordmark { font-size: 19px; }
  .website {
    margin-top: 46px;
    color: #ffffff;
    font-size: 14px;
    letter-spacing: .3em;
  }

  /* Front side */
  .card-front {
    left: 490px; top: 430px;
    width: 630px; height: 360px;
    background: var(--paper);
  }
  .front-decor {
    position: absolute;
    left: 46px; top: 150px;
    width: 170px; height: 170px;
    background: var(--navy);
  }
  .person {
    position: absolute;
    left: 46px; top: 90px;
  }
  .person-name {
    color: var(--navy);
    font-weight: 700;
    font-size: 21px;
    text-transform: uppercase;
    line-height: 1.1;
  }
  .person-title {
    color: var(--grey-text);
    font-size: 15px;
  }
  .card-front .wordmark {
    position: absolute;
    right: 40px; top: 38px;
    font-size: 22px;
    text-align: right;
  }
  .contact {
    position: absolute;
    right: 40px; top: 150px;
    list-style: none;
    text-align: right;
    color: var(--ink);
    font-size: 14px;
    line-height: 1.55;
  }
  .contact li { display: flex; justify-content: flex-end; align-items: center; gap: 8px; }
  .contact .icon { width: 13px; height: 13px; fill: var(--navy); }
  .contact .spacer { width: 13px; }
  .contact .email { margin-top: 12px; }
</style>
</head>
<body>

  <section class="card card-back" aria-label="Card back">
    <div class="back-mark"></div>
    <div class="wordmark">Harbor Wealth Management</div>
    <div class="website">www.harborwmx.com</div>
  </section>

  <section class="card card-front" aria-label="Card front">
    <div class="person">
      <div class="person-name">BriAnne Dockery</div>
      <div class="person-title">Executive Assistant</div>
    </div>
    <div class="front-decor"></div>

    <div class="wordmark">Harbor Wealth Management</div>

    <ul class="contact">
      <li>20537 W. Marlowe PKWY Ste. B<span class="spacer"></span></li>
      <li>Brookvale, HV 77390
        <svg class="icon" viewBox="0 0 16 16" aria-hidden="true"><path d="M3 1h3l1.5 4-2 1.2a9 9 0 0 0 4.3 4.3L11 8.5l4 1.5v3a2 2 0 0 1-2 2A12 12 0 0 1 1 3a2 2 0 0 1 2-2z"/></svg>
      </li>
      <li>(555) 555-0148
        <svg class="icon" viewBox="0 0 16 16" aria-hidden="true"><path d="M4 0h8a1 1 0 0 1 1 1v14a1 1 0 0 1-1 1H4a1 1 0 0 1-1-1V1a1 1 0 0 1 1-1zm1 2v10h6V2H5zm3 11a1 1 0 1 0 0 2 1 1 0 0 0 0-2z"/></svg>
      </li>
      <li>(555) 555-0173
        <svg class="icon" viewBox="0 0 16 16" aria-hidden="true"><path d="M1 3h14v10H1V3zm1.5 1.2L8 8.6l5.5-4.4H2.5z"/></svg>
      </li>
      <li class="email">brianne@harborwmx.com<span class="spacer"></span></li>
    </ul>
  </section>

</body>
</html>
```